Election features for a political website

The Evening Lantern (www.eveninglantern.co.uk)
Web banner designs
Please have a look at The Evening Lantern website (www.eveninglantern.co.uk). We are seeking to add an advertising style banner at the top of every page and post. It will run right across the page (1024 pixels) and be in the region of 200 pixels vertically. (Please advise on what looks best size wise.
The banner will be a slider, operated in a similar way to the current homepage slider. There will be four items on the slider, and so we need four designs that match the aesthetic feel of the website. Each slider will link through to posts on the website.
1.
Headline: OUR CANDIDATE OF THE DAY
Space for a name, head and shoulders picture of the person to be dropped in and a one line reason. This will need to be in an editable format as this image will be changed each day for one month.
2.
Headline: HERO OF THE DAY
Space for name and a one line reason. This will need to be in an editable format as this image will be changed each day for one month.
3.
Headline: VILLAIN OF THE DAY
Space for name of the person to be dropped in and a one line reason. This will need to be in an editable format as this image will be changed each day for one month.
4.
Headline: TEL Poll – [Date]
If the election was today, who would you vote for?
Clickable options:
Harbourites
Meridan
Tallow Assembly
Pomo
Quill
Other
Can a poll widget be added to the banner? We would like this poll to reset each day and then pool the results into a graph day by day over a one month period.
Reason: Payment is now guaranteed. We would like to see more options.

```html
<!DOCTYPE html>
<html lang="en">
<head>
<meta charset="utf-8">
<title>Our Candidate of the Day – Banner</title>
<link href="https://fonts.googleapis.com/css2?family=Arimo:wght@700&family=Tinos:wght@400;700&display=swap" rel="stylesheet">
<style>
  :root {
    --navy: #02558b;
    --band: #1e6494;
    --rule: #0a80cf;
    --white: #ffffff;
    --note: #1f5c8c;
    --photo-light: #d9d9d9;
    --photo-dark: #3a3a3a;
  }
  html, body {
    margin: 0;
    padding: 0;
    width: 1200px;
    height: 420px;
    overflow: hidden;
    background: var(--white);
  }
  .canvas {
    position: relative;
    width: 1200px;
    height: 420px;
  }
  .banner {
    position: absolute;
    left: 12px;
    top: 10px;
    width: 1024px;
    height: 400px;
    background: var(--navy);
  }
  .headline-band {
    position: absolute;
    left: 0;
    top: 55px;
    width: 523px;
    height: 190px;
    background: var(--band);
    border-top: 5px solid var(--rule);
    border-bottom: 5px solid var(--rule);
    box-sizing: border-box;
  }
  .headline {
    position: absolute;
    left: 42px;
    top: 97px;
    margin: 0;
    font-family: "Tinos", "Times New Roman", serif;
    font-weight: 700;
    font-size: 45px;
    line-height: 58px;
    color: var(--white);
    letter-spacing: 0.2px;
  }
  .candidate-name {
    position: absolute;
    left: 42px;
    top: 290px;
    margin: 0;
    font-family: "Arimo", Arial, sans-serif;
    font-weight: 700;
    font-size: 44px;
    line-height: 52px;
    color: var(--white);
  }
  .portrait {
    position: absolute;
    left: 523px;
    top: 12px;
    width: 490px;
    height: 376px;
    background: linear-gradient(120deg, var(--white) 0%, var(--photo-light) 45%, var(--photo-dark) 75%, var(--photo-light) 100%);
  }
  .size-note {
    position: absolute;
    left: 1082px;
    top: 174px;
    margin: 0;
    font-family: "Tinos", "Times New Roman", serif;
    font-weight: 400;
    font-size: 17px;
    line-height: 29px;
    color: var(--note);
  }
</style>
</head>
<body>
  <div class="canvas">
    <section class="banner">
      <div class="headline-band"></div>
      <h1 class="headline">OUR CANDIDATE<br>OF THE DAY</h1>
      <h2 class="candidate-name">MARISSA HOLT</h2>
      <div class="portrait" role="img" aria-label="Head and shoulders photo of the candidate of the day"></div>
    </section>
    <p class="size-note">BANNER<br>SIZE<br>1024x400</p>
  </div>
</body>
</html>
```